Coral Pillow Depot Website

Need a design for a local Coral Pillow Depot store.
The store is called Coral Pillow Depot.
need it to be something that customers can find on the internet and will
give them my location, they need to know i have the same brand mattress as the other store except i have them at almost half the price.

the office phone number is (786)555-0147
the office address is: 4721 sw Heron Glade Ave, Miami FL 33190

included is the logo, id like to stick the with white and teal design

here are is an excerpt that can or cannot be included

"We are a premium mattress discount outlet store located in South Florida; offering Free Delivery to Broward Miami-Dade, the Keys, and Palm Beach.

We carry the best brands in the market: Harlow DreamNest; Brovik SpineEase, Kendal & Pryce, Tarvin, among others.

We are open 7 days a week, and we are accessible from all major highways. We are a family business and our goal is to provide you with the most comfortable and best quality mattress at a price that has no competition. Come visit us and take a look at our large inventory selection."

```html
<!DOCTYPE html>
<html lang="en">
<head>
<meta charset="utf-8">
<title>Coral Pillow Depot</title>
<link rel="stylesheet" href="https://fonts.googleapis.com/css2?family=Arimo:wght@400;700&family=Josefin+Sans:wght@400;600&family=Roboto+Slab:wght@500&display=swap">
<style>
:root{
  --teal:#00afd0;
  --teal-dark:#1a84b0;
  --footer:#3a8e9b;
  --orange:#e8901a;
  --ink:#333;
  --muted:#555;
  --topbar:#1c1c1c;
  --band:#444;
  --panel:#ececec;
}
*{margin:0;padding:0;box-sizing:border-box}
html,body{width:877px;height:1200px;overflow:hidden;background:#fff}
body{position:relative;font-family:Arimo,Arial,sans-serif;color:var(--ink)}
.abs{position:absolute}
.topbar{left:0;top:0;width:877px;height:37px;background:var(--topbar)}
.topbar .phone{left:502px;top:9px;color:#bbb;font-size:15px;font-weight:700;display:flex;align-items:center;gap:5px}
.topbar .quick{left:668px;top:11px;color:#ccc;font-size:13px;word-spacing:2px}
.header{left:0;top:37px;width:877px;height:111px;background:linear-gradient(#fff,#f1f1f1)}
.brand{left:74px;top:39px;display:flex;align-items:center;gap:8px;font-family:"Josefin Sans",sans-serif;font-size:21px;color:#333}
.brand i{width:12px;height:12px;background:var(--teal);display:block}
.nav{left:403px;top:44px;display:flex;align-items:center;font-size:9.5px;color:#222}
.nav span{padding:0 9px;line-height:30px}
.nav .active{background:var(--teal);width:60px;text-align:center;padding:0;margin-right:2px}
.band{left:0;top:148px;width:877px;height:219px;background:var(--band)}
.slide{left:74px;top:171px;width:729px;height:312px;border:6px solid var(--teal);background:#fff;box-shadow:0 12px 14px -8px rgba(0,0,0,.35)}
.slide .photo{position:absolute;inset:0;background:linear-gradient(170deg,#8fb3bb 0%,#d9d2c0 30%,#f3efe6 55%,#ece6da 100%)}
.slide .headline{position:absolute;left:94px;top:222px;font-weight:700;font-size:21.5px;line-height:26px;color:var(--teal-dark);text-transform:uppercase;white-space:nowrap}
.headline .hot{color:var(--orange)}
.dots{left:400px;top:494px;display:flex;gap:6px}
.dots i{width:15px;height:15px;border-radius:50%;background:#ddd;border:1px solid #bbb;display:block}
.dots i.on{background:var(--teal)}
.rule{left:73px;top:527px;width:731px;height:1px;background:#ddd}
.office{left:75px;top:573px;width:155px;height:267px;box-shadow:2px 0 3px rgba(0,0,0,.06)}
.office .bar{height:27px;background:#a7b0ad;font-size:6px;color:#eee;padding:9px 12px;display:flex;justify-content:space-between}
.office h3{font-weight:400;font-size:13px;color:#444;margin:24px 0 0 15px}
.office .map{margin:10px 0 0 18px;width:100px;height:66px;background:linear-gradient(#d8d8d8,#a9a9a9);border-radius:4px}
.office .addr{margin:22px 0 0 18px;font-size:10px;line-height:13px;color:#444;letter-spacing:.3px}
.office .addr b{color:#1d2b50;display:block;margin-bottom:2px}
.office .btn{margin:10px 0 0 18px;width:70px;height:15px;background:#3b4148;color:#fff;font-size:7.5px;padding:3px 6px;display:flex;justify-content:space-between}
.about{left:267px;top:573px;width:366px}
.about h2{font-family:"Josefin Sans",sans-serif;font-weight:400;font-size:14.5px;line-height:18px;color:var(--teal-dark);letter-spacing:.5px;text-transform:uppercase}
.about .lede{font-size:8.6px;line-height:14.6px;color:var(--muted);margin-top:8px}
.about .pitch{font-size:12.5px;line-height:14.6px;color:#333;margin-top:5px}
.hours{left:652px;top:575px;width:151px;height:168px;border:1px solid #ddd;text-align:center}
.hours h4{font-family:"Josefin Sans",sans-serif;font-weight:400;font-size:13px;color:#333;text-align:left;padding:17px 0 0 8px;height:42px;border-bottom:1px solid #ddd;letter-spacing:.6px;white-space:nowrap}
.hours .swoosh{position:absolute;right:3px;top:4px;width:22px;height:22px;background:linear-gradient(135deg,var(--teal),#cfeaf0);border-radius:0 0 0 22px}
.hours p{font-size:14px;line-height:17.5px;color:#666;padding:13px 6px 0}
.hours b{color:var(--teal);display:block;letter-spacing:.4px}
.brands{left:92px;top:869px;width:689px;height:144px;background:var(--panel);border:1px solid #d5d5d5;border-radius:4px}
.brands h2{position:absolute;left:23px;top:18px;font-family:"Josefin Sans",sans-serif;font-weight:400;font-size:15.5px;color:#333;letter-spacing:1px}
.tiles{position:absolute;left:24px;top:47px;display:flex;gap:10px}
.tile{width:152px;height:78px;background:#fff;border:3px solid #fff;box-shadow:0 0 0 1px #ddd;display:flex;align-items:center;justify-content:center;gap:6px;font-size:14px;font-weight:700;color:#3a3a3a;white-space:nowrap}
.tile i{width:10px;height:10px;background:var(--teal);display:block}
.arrow{top:71px;width:32px;height:32px;border-radius:50%;background:#fff;border:2px solid #888}
.arrow svg{display:block;margin:7px auto}
.footer{left:0;top:1054px;width:877px;height:146px;background:var(--footer)}
.store{left:87px;top:1065px;color:#fff}
.store h3{font-family:"Roboto Slab",serif;font-weight:500;font-size:15.5px;letter-spacing:1px}
.store ul{list-style:none;margin:7px 0 0 5px;font-size:11px;line-height:14.6px}
.contact{left:268px;top:1054px;width:536px;height:94px;background:var(--teal);border-top:6px solid #b0b0b0}
.contact h3{position:absolute;top:12px;font-size:15px;font-weight:700;color:#1f5f6e}
.contact .addr{position:absolute;left:19px;top:32px;font-size:10.5px;line-height:14px;color:#fff}
.social{position:absolute;left:180px;top:36px;display:flex;gap:2px}
.social i{width:23px;height:23px;border-radius:4px;background:#fff;opacity:.85;display:block}
.copy{position:absolute;left:361px;top:35px;font-size:10px;line-height:16px;color:#fff}
.links{left:441px;top:1162px;font-size:10px;color:#fff;word-spacing:2px}
</style>
</head>
<body>
<div class="abs topbar">
  <div class="abs phone"><svg width="14" height="12" viewBox="0 0 14 12"><path d="M1 4 Q7 -1 13 4 L11 6 L9 4 L5 4 L3 6 Z M4 6 H10 L12 11 H2 Z" fill="#bbb"/></svg>(786)555-0147</div>
  <div class="abs quick">FAQ |&nbsp; Contact |&nbsp; Blog</div>
</div>
<header class="abs header">
  <div class="abs brand"><i></i>Coral Pillow Depot</div>
  <nav class="abs nav">
    <span class="active">HOME</span><span>WE ARE MATTRESS</span><span>DISCOUNTERS</span><span>LOCATION</span><span>GET IN TOUCH</span>
  </nav>
</header>
<div class="abs band"></div>
<section class="abs slide">
  <div class="photo" role="img" aria-label="Photo of a white memory foam mattress with blue pillows and a teal throw"></div>
  <p class="headline"><span class="hot">Same brand mattress</span> as the other store<br>except I have them <span class="hot">at almost half the price</span></p>
</section>
<div class="abs dots"><i></i><i class="on"></i><i></i></div>
<div class="abs rule"></div>
<aside class="abs office">
  <div class="bar"><span>II</span><span>01 02 03 04</span></div>
  <h3>Office Location</h3>
  <div class="map" role="img" aria-label="Dotted world map with a location pin"></div>
  <div class="addr"><b>The Office Address:</b>4721 sw Heron Glade Ave<br>Miami FL 33190<br><span style="display:block;margin-top:3px">Tel: (786)555-0147</span></div>
  <div class="btn"><span>Spot Us</span><span>›</span></div>
</aside>
<main class="abs about">
  <h2>We are a family business and our goal is to provide you with the most comfortable and best quality mattress</h2>
  <p class="lede">Based in Stafford, Texas, we design, provide, and service licensed and unlicensed, point-to-point and point-to-multipoint microwave systems. For over 40 years, Relay Span Systems has built and delivered mission critical microwave communications product-sLorem Ipsum is simply dummy text of the printing and typesetting industry. Lorem Ipsum has been the industry's standard dummy text ever since the 1500s, when an unknown printer took a galley of type and scrambled it to make a type specimen book. It has survived not only five centuries, but also the leap into electronic typesetting, remaining essentially unchanged.</p>
  <p class="pitch">We are a premium mattress discount outlet store located in South Florida; offering Free Delivery to Broward Miami-Dade, the Keys, and Palm Beach</p>
</main>
<aside class="abs hours">
  <h4>OPENING TIME</h4>
  <div class="swoosh" role="img" aria-label="Teal swoosh decoration"></div>
  <p>WE ARE OPEN<b>7 DAYS A WEEK</b>and we are acces-sible from all major highways</p>
</aside>
<section class="abs brands">
  <h2>WE CARRY THE BEST BRANDS IN THE MARKET</h2>
  <div class="tiles">
    <div class="tile"><i></i>Harlow DreamNest</div>
    <div class="tile"><i></i>Brovik SpineEase</div>
    <div class="tile"><i></i>Kendal &amp; Pryce</div>
    <div class="tile"><i></i>Tarvin</div>
  </div>
  <div class="abs arrow" style="left:-14px"><svg width="12" height="14"><path d="M10 1 L3 7 L10 13" stroke="#555" stroke-width="3" fill="none"/></svg></div>
  <div class="abs arrow" style="left:671px"><svg width="12" height="14"><path d="M2 1 L9 7 L2 13" stroke="#555" stroke-width="3" fill="none"/></svg></div>
</section>
<footer class="abs footer"></footer>
<div class="abs store">
  <h3>STORE HOURS</h3>
  <ul><li>Mon. 9 a.m - 5 p.m</li><li>Tue.&nbsp; 9 a.m - 5 p.m</li><li>Wed. 9 a.m - 5 p.m</li><li>Thu.&nbsp; 9 a.m - 5 p.m</li><li>Fri.&nbsp;&nbsp;&nbsp; 9 a.m - 5 p.m</li><li>Sat.&nbsp; 9 a.m - 5 p.m</li></ul>
</div>
<div class="abs contact">
  <h3 style="left:19px">Get in touch</h3>
  <p class="addr">4721 sw Heron Glade Ave,<br>&nbsp;Miami FL 33190<br><span style="display:block;margin-top:3px">&nbsp;(786)555-0147</span></p>
  <h3 style="left:181px">Follow&nbsp; us</h3>
  <div class="social" aria-label="Social links"><i></i><i></i><i></i><i></i><i></i><i></i></div>
  <p class="copy">© 2014 Copyright - Coral Pillow Depot.<br>&nbsp;All rights reserved</p>
</div>
<div class="abs links">Home&nbsp; ~&nbsp; Newsletter&nbsp; ~&nbsp; Press&nbsp; ~&nbsp; Contact Us&nbsp; ~&nbsp; Terms of Use&nbsp; ~&nbsp; Credits</div>
</body>
</html>
```